Small Unique Manufacturer Needs a facelift for eCommerce Wordpress Site

We need a wordpress template design that brands our business based in Minneapolis, MN called "Lantern Fables". Lantern Fables manufacturers and assembles fraternity and sorority paddle kits for Sisterhood parties and fraternity rush and pledge process decoration parties. We're our site is an eCommerce site that runs at LanternFables.com. We'd like an attractive design that's more on the feminine side (rather than masculine) as our primary consumer will be female. However as we move into the future we will have products for the fraternities as well.
We like earthy neutral colors, our products are unfinished pine, walnut, and oak, but we're not keen on focusing on woodgrain designs, etc.
The final design should communicate fun, be clean, clear, and bright, and appeal to the millennial generation and must be fully functional.
We're currently using the WooCommerce plugin for our eCommerce back end and like it.

Target Market(s)

College greeks. Fraternity and Sorority Members

Industry/Entity Type

Business

Font styles to use
Sans Serif

Colors
cde8f3
ecf7fa
f9d9e8
fbc994

Requirements
Must have
• Clean, clear design. A nice branding project start to finish. Millennial focus.
• Must work with our current WooCommerce page.
Should not have
• Anything that looks down or talks down to college students.

```html
<!DOCTYPE html>
<html lang="en">
<head>
<meta charset="utf-8">
<title>Lantern Fables — Home</title>
<link href="https://fonts.googleapis.com/css2?family=Open+Sans:ital,wght@0,400;0,600;0,700;1,400&display=swap" rel="stylesheet">
<style>
:root{
  --pink:#f9d9e8;
  --blue:#0aa9d3;
  --navy:#1679bf;
  --deep:#0f5f9a;
  --orange:#f7782a;
  --peach:#fbc994;
  --ink:#333333;
  --muted:#666666;
  --line:#c9c9c9;
  --band:#f1f1f1;
  --foot:#c9c9cc;
}
*{box-sizing:border-box;margin:0;padding:0}
html,body{width:954px;height:1200px;overflow:hidden;background:#fff}
body{position:relative;font-family:"Open Sans",Arial,sans-serif;color:var(--ink)}
.abs{position:absolute}
.top-band{left:0;top:0;width:954px;height:294px;background:var(--pink)}
.brand-mark{left:163px;top:16px;width:71px;height:72px;background:var(--orange);border-radius:6px;display:flex;align-items:center;padding:0 7px;color:#fff;font-weight:700;font-size:14px;line-height:16px;overflow:hidden}
.bag{right:162px;top:16px;display:flex;gap:6px;font-size:8px;line-height:12px;text-align:right;color:#222}
.bag-text{text-align:left}
.bag-text .link{display:block;text-align:right;margin-left:-60px}
.call{right:162px;top:59px;display:flex;align-items:center;gap:8px;font-size:15px;color:var(--blue)}
.call b{font-weight:400;color:#555}
.nav{left:163px;top:103px;width:629px;height:23px;background:#fff;border:1px solid var(--line);display:flex;justify-content:center;gap:31px;font-size:9px;line-height:21px;letter-spacing:.2px;color:#222}
.nav .current{color:var(--navy);border-bottom:1px solid var(--navy);height:20px}
.hero{left:162px;top:131px;width:630px;height:256px;background:#fff;border:1px solid var(--line);overflow:hidden;box-shadow:0 22px 18px -14px rgba(0,0,0,.18)}
.hero-art{position:absolute;left:14px;top:22px;width:300px;height:210px;border-radius:30px;background:radial-gradient(ellipse at center,#d9a46a 0%,#b9773e 60%,rgba(185,119,62,0) 75%)}
.hero-panel{position:absolute;left:0;top:0}
.hero-copy{position:absolute;right:28px;top:48px;width:230px;text-align:right;color:#fff}
.hero-copy h2{font-size:17px;font-weight:600;text-align:center;margin-left:30px;margin-bottom:14px}
.hero-copy p{font-size:10px;line-height:16px;font-weight:400;color:#eaf7fb}
.shop-btn{display:inline-block;margin-top:25px;margin-right:44px;width:123px;height:34px;line-height:34px;text-align:center;background:var(--deep);color:#fff;font-size:16px;font-weight:600;border-radius:2px}
.dots{position:absolute;left:296px;top:246px;display:flex;gap:3px}
.dots i{width:7px;height:7px;border-radius:50%;background:#b8b8b8}
.dots i.on{background:var(--blue)}
.cat-head{left:162px;top:446px;width:110px;height:34px;background:var(--navy);color:#fff;font-size:16px;font-weight:600;line-height:34px;text-align:center}
.cat-list{left:165px;top:495px;list-style:none;font-size:12px;color:#555}
.cat-list li{height:30.5px;line-height:18px}
.cat-list li::before{content:"";display:inline-block;border-left:4px solid #777;border-top:3px solid transparent;border-bottom:3px solid transparent;margin-right:7px;vertical-align:1px}
.see-all{left:760px;top:444px;font-size:10px;color:var(--navy)}
.card{width:118px;height:110px;border:2px solid var(--blue);border-bottom:none;background:#fff}
.card-img{position:absolute;left:42px;top:8px;width:28px;height:70px;border-radius:8px;transform:rotate(25deg);background:linear-gradient(180deg,#d7a35c,#a8742f)}
.card-label{position:absolute;left:-2px;bottom:0;width:118px;height:27px;background:var(--peach);font-size:10px;line-height:27px;padding-left:10px;color:#222}
.card-basket{position:absolute;right:0;top:0;width:31px;height:27px;background:var(--navy);display:flex;align-items:center;justify-content:center}
.pager{left:751px;top:771px;display:flex;gap:5px}
.newsletter{left:0;top:864px;width:954px;height:77px;background:var(--band)}
.news-text{left:174px;top:885px;font-size:16px;line-height:23px;color:var(--navy);font-weight:400}
.news-form{left:526px;top:890px;width:254px;height:32px;border:2px solid var(--blue);background:#fff;display:flex}
.news-form span{flex:1;font-size:10px;font-style:italic;color:#7fcbe6;line-height:28px;padding-left:24px}
.news-form i{width:42px;border-left:2px solid var(--blue);display:flex;align-items:center;justify-content:center}
.foot-col h3{font-size:16px;font-weight:400;color:#222;margin-bottom:18px;white-space:nowrap}
.foot-col h3 em{font-style:normal;color:var(--peach)}
.foot-col p{font-size:9.5px;line-height:14.5px;color:#444}
.foot-links{list-style:none;font-size:9.5px;color:#555;line-height:20px}
.contact-list{list-style:none;font-size:9px;color:#555}
.contact-list li{height:21.5px;display:flex;gap:9px}
.contact-list li .ic{width:12px;display:inline-block}
.bottom-bar{left:0;top:1163px;width:954px;height:37px;background:var(--foot)}
.copyright{left:162px;top:1174px;font-size:10px;color:#444}
.social{left:712px;top:1174px;display:flex;gap:7px}
.social i{width:14px;height:14px;border-radius:50%;background:var(--navy)}
</style>
</head>
<body>
<div class="abs top-band"></div>

<header>
  <div class="abs brand-mark">Lantern Fables</div>
  <div class="abs bag">
    <svg width="18" height="22" viewBox="0 0 18 22"><path d="M5 6V4a4 4 0 0 1 8 0v2" fill="none" stroke="#0aa9d3" stroke-width="1.6"/><rect x="1" y="6" width="16" height="15" rx="1" fill="#0aa9d3"/></svg>
    <div class="bag-text">Shopping Bag:<br>0 Items - $0.00<span class="link">View Bag &amp; Checkout</span></div>
  </div>
  <div class="abs call">
    <svg width="31" height="31" viewBox="0 0 31 31"><circle cx="15.5" cy="15.5" r="14" fill="none" stroke="#0aa9d3" stroke-width="2"/><path d="M10 8.5c1-1 2-1 2.6 0l1.6 2.6c.4.7.2 1.4-.5 1.9l-1 .7c.8 2 2.3 3.6 4.2 4.5l.8-1c.5-.7 1.3-.8 1.9-.4l2.5 1.7c.9.6.9 1.7 0 2.6-1.7 1.7-4 1.7-6.8-.2-3-2-5-4.8-5.9-7.6-.6-1.9-.4-3.7.6-4.8z" fill="#0aa9d3"/></svg>
    <span>Call Us <b>012-555-0148</b></span>
  </div>
  <nav class="abs nav">
    <span class="current">HOME</span><span>PRODUCTS</span><span>ABOUT US</span><span>GALLERY</span><span>CONTACT US</span>
  </nav>
</header>

<section class="abs hero">
  <div class="hero-art" role="img" aria-label="Row of engraved wooden sorority paddles with crests and names"></div>
  <svg class="hero-panel" width="630" height="256" viewBox="0 0 630 256"><polygon points="329,0 630,0 630,256 339,256 394,127" fill="#0aa9d3"/></svg>
  <div class="hero-copy">
    <h2>Pellentesque accumsan</h2>
    <p>Lorem ipsum is a dummy text only.<br>Dolor sit amet, consectetur<br>adipiscing elit. Nullam felis mauris,<br>eleifend ac rhoncus non,</p>
    <span class="shop-btn">Shop Now</span>
  </div>
  <div class="dots"><i></i><i class="on"></i><i></i><i></i></div>
</section>

<aside>
  <div class="abs cat-head">Categories</div>
  <ul class="abs cat-list">
    <li>Pellentesque</li><li>Accumsan</li><li>Dignissim</li><li>Libero eu</li><li>Dignissim</li><li>Aliquam sed</li><li>Accumsan</li>
  </ul>
</aside>

<main>
  <span class="abs see-all">See all</span>
  <div class="abs card" style="left:345px;top:480px"><div class="card-img" role="img" aria-label="Wooden paddle product"></div><div class="card-label">Lorem Ipsum<span class="card-basket"><svg width="16" height="13" viewBox="0 0 16 13"><path d="M1 5h14l-2 7H3z M4 5l4-4 4 4" fill="none" stroke="#fff" stroke-width="1.4"/></svg></span></div></div>
  <div class="abs card" style="left:482px;top:480px"><div class="card-img" role="img" aria-label="Wooden paddle product"></div><div class="card-label">Lorem Ipsum<span class="card-basket"><svg width="16" height="13" viewBox="0 0 16 13"><path d="M1 5h14l-2 7H3z M4 5l4-4 4 4" fill="none" stroke="#fff" stroke-width="1.4"/></svg></span></div></div>
  <div class="abs card" style="left:618px;top:480px"><div class="card-img" role="img" aria-label="Wooden paddle product"></div><div class="card-label">Lorem Ipsum<span class="card-basket"><svg width="16" height="13" viewBox="0 0 16 13"><path d="M1 5h14l-2 7H3z M4 5l4-4 4 4" fill="none" stroke="#fff" stroke-width="1.4"/></svg></span></div></div>
  <div class="abs card" style="left:345px;top:623px"><div class="card-img" role="img" aria-label="Wooden paddle product"></div><div class="card-label">Lorem Ipsum<span class="card-basket"><svg width="16" height="13" viewBox="0 0 16 13"><path d="M1 5h14l-2 7H3z M4 5l4-4 4 4" fill="none" stroke="#fff" stroke-width="1.4"/></svg></span></div></div>
  <div class="abs card" style="left:482px;top:623px"><div class="card-img" role="img" aria-label="Wooden paddle product"></div><div class="card-label">Lorem Ipsum<span class="card-basket"><svg width="16" height="13" viewBox="0 0 16 13"><path d="M1 5h14l-2 7H3z M4 5l4-4 4 4" fill="none" stroke="#fff" stroke-width="1.4"/></svg></span></div></div>
  <div class="abs card" style="left:618px;top:623px"><div class="card-img" role="img" aria-label="Wooden paddle product"></div><div class="card-label">Lorem Ipsum<span class="card-basket"><svg width="16" height="13" viewBox="0 0 16 13"><path d="M1 5h14l-2 7H3z M4 5l4-4 4 4" fill="none" stroke="#fff" stroke-width="1.4"/></svg></span></div></div>
  <div class="abs pager">
    <svg width="17" height="17" viewBox="0 0 17 17"><circle cx="8.5" cy="8.5" r="8.5" fill="#b5b5b5"/><path d="M12 8.5H5M8 5.3 4.8 8.5 8 11.7" fill="none" stroke="#fff" stroke-width="2"/></svg>
    <svg width="17" height="17" viewBox="0 0 17 17"><circle cx="8.5" cy="8.5" r="8.5" fill="#1679bf"/><path d="M5 8.5h7M9 5.3l3.2 3.2L9 11.7" fill="none" stroke="#fff" stroke-width="2"/></svg>
  </div>
</main>

<section>
  <div class="abs newsletter"></div>
  <p class="abs news-text">Sign up to our newsletter and receive<br>discounts and special offers</p>
  <div class="abs news-form"><span>Enter email address</span><i><svg width="18" height="18" viewBox="0 0 17 17"><circle cx="8.5" cy="8.5" r="8.5" fill="#0aa9d3"/><path d="M4.5 8.5h7M8.5 5.3l3.2 3.2-3.2 3.2" fill="none" stroke="#fff" stroke-width="2"/></svg></i></div>
</section>

<footer>
  <div class="abs foot-col" style="left:231px;top:990px;width:160px">
    <h3>About <em>Lantern Fables</em></h3>
    <p>Lorem ipsum is a dummy text only. Dolor sit amet, consectetur adipiscing elit. Nullam felis mauris, eleifend ac rhoncus non, lobortis at diam.</p>
  </div>
  <div class="abs foot-col" style="left:459px;top:990px">
    <h3>Quick Links</h3>
    <ul class="foot-links"><li>Home</li><li>About Us</li><li>Our Products</li><li>View Gallery</li><li>Contact Us</li></ul>
  </div>
  <div class="abs foot-col" style="left:600px;top:990px">
    <h3 style="margin-left:10px">Contact Us</h3>
    <ul class="contact-list">
      <li><span class="ic"><svg width="11" height="10" viewBox="0 0 11 10"><path d="M5.5 0 11 5H9.5v5h-3V7h-2v3h-3V5H0z" fill="#1679bf"/></svg></span>Mira T. Holloway</li>
      <li><span class="ic"></span>48 Willow Row</li>
      <li><span class="ic"></span>Northfield, MN 55057</li>
      <li><span class="ic"><svg width="7" height="11" viewBox="0 0 7 11"><rect x=".7" y=".7" width="5.6" height="9.6" rx="1" fill="none" stroke="#1679bf" stroke-width="1.4"/></svg></span>0845 555 0192</li>
      <li><span class="ic"><svg width="11" height="8" viewBox="0 0 11 8"><rect width="11" height="8" fill="#1679bf"/><path d="M0 0l5.5 4.5L11 0" fill="none" stroke="#fff" stroke-width="1"/></svg></span>contact@example.com</li>
    </ul>
  </div>
  <div class="abs bottom-bar"></div>
  <p class="abs copyright">Copyright©lanternfables. All Rights Reserved. 2014</p>
  <div class="abs social"><i></i><i></i><i></i><i></i></div>
</footer>
</body>
</html>
```